BRIM Outreach Partners Business Card Rebrand

Hello Designers! We are looking for help designing our new business card to go in conjunction with our company rebrand. Unfortunately, we have an event mid June that requires we get these printed ASAP (before our new website is launched.) We have a mostly complete Brand Book which I have uploaded to this request for your reference to company information, style, fonts. I've also enclosed our logo file in .eps & .jpg. Attached is a sample business card my boss liked but said was "too simple." I made it in Canva and do not profess to be a designer. NOT FOR DESIGN REFERENCE, ONLY FOR CONTEXT Here is what our old website looks like: https://brimoutreachpartners.com/.

```html
<!DOCTYPE html>
<html lang="en">
<head>
<meta charset="utf-8">
<title>BRIM Outreach Partners – Business Card</title>
<link href="https://fonts.googleapis.com/css2?family=Lato:wght@400;700;900&display=swap" rel="stylesheet">
<style>
  :root {
    --page: #2a2c2f;
    --card: #1c1c1e;
    --blue: #4ab3e6;
    --white: #ffffff;
    --soft: #d9d9d9;
    --rule: #6a6a6a;
  }
  * { box-sizing: border-box; margin: 0; padding: 0; }
  html, body { width: 1200px; height: 952px; overflow: hidden; }
  body {
    background: var(--page);
    font-family: "Lato", Arial, sans-serif;
    display: flex;
    flex-direction: column;
    align-items: center;
    justify-content: center;
    gap: 52px;
  }
  .card {
    position: relative;
    width: 700px;
    height: 400px;
    background: var(--card);
    border-radius: 26px;
    overflow: hidden;
    box-shadow: 0 10px 30px rgba(0,0,0,.45);
  }
  .edge-band {
    position: absolute;
    left: 0; bottom: 0;
    width: 100%;
    height: 40px;
  }
  .brand {
    position: absolute;
    display: flex;
    align-items: center;
  }
  .brand-dot {
    border-radius: 50%;
    background: var(--blue);
    flex: none;
  }
  .brand-name {
    color: var(--white);
    font-weight: 900;
    line-height: 1.05;
  }
  /* front */
  .card-front .brand { left: 0; right: 0; top: 140px; justify-content: center; gap: 22px; }
  .card-front .brand-dot { width: 84px; height: 84px; }
  .card-front .brand-name { font-size: 44px; }
  /* back */
  .card-back .brand { left: 36px; top: 92px; gap: 14px; }
  .card-back .brand-dot { width: 56px; height: 56px; }
  .card-back .brand-name { font-size: 26px; width: 190px; }
  .contact {
    position: absolute;
    left: 330px;
    top: 80px;
    color: var(--soft);
  }
  .contact-name {
    color: var(--blue);
    font-weight: 700;
    font-size: 25px;
    letter-spacing: .5px;
    text-transform: uppercase;
  }
  .contact-title { font-size: 19px; color: var(--soft); margin-top: 2px; }
  .contact-rule { width: 44px; height: 2px; background: var(--rule); margin: 9px 0; }
  .contact-base { font-size: 16px; margin-bottom: 14px; }
  .contact-row {
    display: flex;
    align-items: center;
    gap: 12px;
    font-size: 17px;
    margin-bottom: 9px;
  }
  .contact-icon {
    width: 22px; height: 22px;
    background: var(--blue);
    border-radius: 3px;
    display: flex; align-items: center; justify-content: center;
    flex: none;
  }
</style>
</head>
<body>

  <section class="card card-front" aria-label="Card front">
    <div class="brand">
      <span class="brand-dot"></span>
      <span class="brand-name">BRIM Outreach<br>Partners</span>
    </div>
    <svg class="edge-band" viewBox="0 0 700 40" preserveAspectRatio="none" aria-hidden="true">
      <polygon points="0,12 320,12 326,24 0,24" fill="var(--blue)"/>
      <polygon points="326,17 700,17 700,20 326,20" fill="var(--white)"/>
    </svg>
  </section>

  <section class="card card-back" aria-label="Card back">
    <div class="brand">
      <span class="brand-dot"></span>
      <span class="brand-name">BRIM Outreach Partners</span>
    </div>
    <div class="contact">
      <p class="contact-name">Daniel Ortega-Hale</p>
      <p class="contact-title">Managing Partner</p>
      <div class="contact-rule"></div>
      <p class="contact-base">Denver, CO based (Mountain Time)</p>
      <p class="contact-row">
        <span class="contact-icon">
          <svg width="14" height="14" viewBox="0 0 24 24"><path fill="#fff" d="M6.6 10.8a15 15 0 0 0 6.6 6.6l2.2-2.2c.3-.3.7-.4 1-.2 1.1.4 2.3.6 3.6.6.6 0 1 .4 1 1V20c0 .6-.4 1-1 1A17 17 0 0 1 3 4c0-.6.4-1 1-1h3.5c.6 0 1 .4 1 1 0 1.3.2 2.5.6 3.6.1.3 0 .7-.2 1z"/></svg>
        </span>+945-310-4172
      </p>
      <p class="contact-row">
        <span class="contact-icon">
          <svg width="14" height="14" viewBox="0 0 24 24"><path fill="none" stroke="#fff" stroke-width="2.2" d="M3 6h18v12H3zM3 6l9 7 9-7"/></svg>
        </span>daniel@brimoutreachpartners.com
      </p>
      <p class="contact-row">
        <span class="contact-icon">
          <svg width="14" height="14" viewBox="0 0 24 24"><path fill="#fff" d="M5 3l14 8-6 1.5L10 19z"/></svg>
        </span>brimoutreachpartners.com
      </p>
    </div>
    <svg class="edge-band" viewBox="0 0 700 40" preserveAspectRatio="none" aria-hidden="true">
      <polygon points="0,17 300,17 300,20 0,20" fill="var(--white)"/>
      <polygon points="300,12 700,12 700,24 306,24" fill="var(--blue)"/>
    </svg>
  </section>

</body>
</html>
```